First Aid Training business needs business card design

We would like a double sided business card designed for a first aid training business - Brindlewood First Aid. We provide first aid training and , WHS (work, health and safety) training.

The attached word document contains the key information we would like on each side of the business card.

Final design needs to be delivered in print ready format, along with the original file.

```html
<!DOCTYPE html>
<html lang="en">
<head>
<meta charset="utf-8">
<title>Brindlewood First Aid – Business Card</title>
<link rel="stylesheet" href="https://fonts.googleapis.com/css2?family=Montserrat:wght@500&family=Catamaran:wght@700&family=Mulish:wght@700&display=swap">
<style>
  :root {
    --page: #ffffff;
    --frame: #a7a8ab;
    --card: #ffffff;
    --red: #ec2227;
    --black: #000000;
    --ink: #111111;
    --light: #ffffff;
    --ghost: rgba(120, 120, 120, 0.14);
  }
  html, body {
    margin: 0;
    padding: 0;
    width: 1200px;
    height: 1200px;
    overflow: hidden;
    background: var(--page);
  }
  .canvas {
    position: relative;
    width: 1200px;
    height: 1200px;
  }
  .card-frame {
    position: absolute;
    left: 149px;
    top: 338px;
    width: 900px;
    height: 540px;
    background: var(--frame);
  }
  .card {
    position: absolute;
    left: 30px;
    top: 30px;
    width: 840px;
    height: 478px;
    background: var(--card);
    overflow: hidden;
  }
  .card-graphics {
    position: absolute;
    inset: 0;
  }
  .brand {
    position: absolute;
    left: 150px;
    top: 52px;
    display: flex;
    align-items: center;
    gap: 38px;
  }
  .brand-dot {
    width: 140px;
    height: 140px;
    border-radius: 50%;
    background: var(--red);
  }
  .brand-name {
    font-family: "Montserrat", sans-serif;
    font-weight: 500;
    color: var(--ink);
    line-height: 1;
    margin: 0;
  }
  .brand-name .line-main {
    display: block;
    font-size: 41px;
    letter-spacing: 0.5px;
  }
  .brand-name .line-sub {
    display: block;
    font-size: 25.5px;
    margin-top: 8px;
    letter-spacing: 0.3px;
  }
  .person-name {
    position: absolute;
    left: 0;
    width: 808px;
    top: 208px;
    text-align: center;
    margin: 0;
    font-family: "Catamaran", sans-serif;
    font-weight: 700;
    font-size: 38px;
    color: var(--ink);
    line-height: 1;
  }
  .contact {
    position: absolute;
    left: 37px;
    top: 306px;
    margin: 0;
    padding: 0;
    list-style: none;
    font-family: "Mulish", sans-serif;
    font-weight: 700;
    font-size: 26px;
    letter-spacing: 2.6px;
    color: var(--light);
    line-height: 34px;
  }
</style>
</head>
<body>
<main class="canvas">
  <section class="card-frame">
    <article class="card">
      <svg class="card-graphics" width="840" height="478" viewBox="0 0 840 478" aria-hidden="true">
        <polygon fill="var(--red)" points="0,266 458,266 580,435 0,435"/>
        <polygon fill="var(--black)" points="0,435 580,435 611,478 0,478"/>
        <polygon fill="var(--black)" points="483,266 840,266 840,435 604,435"/>
        <polygon fill="var(--red)" points="604,435 840,435 840,478 635,478"/>
        <circle class="ghost-circle" cx="640" cy="300" r="140" fill="var(--ghost)"/>
      </svg>

      <header class="brand">
        <span class="brand-dot" aria-hidden="true"></span>
        <h1 class="brand-name">
          <span class="line-main">BRINDLEWOOD</span>
          <span class="line-sub">FIRST AID TRAINING</span>
        </h1>
      </header>

      <h2 class="person-name">Daniel Hartley</h2>

      <ul class="contact">
        <li class="contact-phone">0400 555 218</li>
        <li class="contact-email">help@brindlewoodaid.com</li>
        <li class="contact-web">brindlewoodaid.com.au</li>
      </ul>
    </article>
  </section>
</main>
</body>
</html>
```